Italian restaurant needs new site

Need to make our website better.

Must have reservation module

Must be able to sell wine tasting tours and wine pairing tours and intégrate with lumo desk

Blog

Social media

Wandermeter ranking and last review.

Number of Pages Required

1 page

Font styles to use
Serif

Requirements
Must have
• Reservation module
• Marketplace to buy wine pairings and gift certificates
• Wandermeter review
• Chatterbay posts
• All info from old site

```html
<!DOCTYPE html>
<html lang="en">
<head>
<meta charset="utf-8">
<title>Vellora Bistro – Italian Restaurant in Cabo San Lucas</title>
<link rel="stylesheet" href="https://fonts.googleapis.com/css2?family=Roboto:wght@700&family=Open+Sans:wght@400;600&family=Philosopher:wght@400;700&family=Josefin+Sans:wght@300;600;700&family=Lora:ital@1&display=swap">
<style>
:root{
  --wine:#5a0b13;
  --wine-deep:#2a0508;
  --red:#c23a2f;
  --red-text:#b8302a;
  --gold:#e9d08c;
  --gold-deep:#d9b862;
  --cream:#f4ecdf;
  --olive:#8f7d16;
  --ink:#1a0a08;
  --blue:#3b78d8;
  --text-light:#f1e6e0;
  --grey-text:#6a6058;
}
*{box-sizing:border-box;margin:0;padding:0}
html,body{width:1200px;height:1200px;overflow:hidden;background:#fff}
body{position:relative;font-family:"Open Sans",sans-serif}
.abs{position:absolute}
.sc{font-family:"Philosopher",serif;font-variant:small-caps}

/* ===== large hero ===== */
.hero{left:0;top:0;width:1200px;height:576px;overflow:hidden}
.hero-photo{left:0;top:0;width:1200px;height:535px;
  background:radial-gradient(ellipse at 55% 40%,#a3202c 0%,#6e0f1a 40%,#3a060c 80%),#3a060c}
.hero-base{left:0;top:535px;width:534px;height:41px;background:#0d0204}
.hero-nav{left:0;top:0;width:1200px;height:45px;background:rgba(30,4,8,.55)}
.hero-nav a{position:absolute;top:13px;color:#fff;font-size:15px;text-decoration:none}
.hero-nav .sep{position:absolute;top:6px;width:1px;height:37px;background:rgba(255,255,255,.18)}
.hero-logo{left:552px;top:0;width:176px;height:66px}
.hero-logo span{position:absolute;left:0;top:44px;width:176px;text-align:center;font-family:"Philosopher",serif;font-size:17px;color:#5a0b13}
.hero-hours{left:928px;top:54px;font-family:"Lora",serif;font-style:italic;font-size:11px;color:var(--gold)}
.hero-title{left:102px;top:144px;font-family:"Roboto",sans-serif;font-weight:700;font-size:45px;line-height:47px;color:#fff;letter-spacing:.5px}
.hero-copy{left:108px;top:307px;width:380px;font-size:13px;line-height:23.2px;color:var(--text-light)}
.btn-gold{background:var(--gold);color:var(--ink);clip-path:polygon(0 0,100% 0,95% 100%,0 100%)}
.hero-btn{left:106px;top:499px;width:84px;height:24px;font-size:13px;line-height:24px;padding-left:9px}

/* ===== page mockup ===== */
.page{left:534px;top:66px;width:626px;height:1131px;overflow:hidden;background:#fff}

.p-hero{left:0;top:0;width:626px;height:288px;overflow:hidden}
.p-hero-photo{left:0;top:0;width:626px;height:288px;
  background:radial-gradient(ellipse at 60% 45%,#9c1f2a 0%,#5e0d16 50%,#2c0509 90%)}
.p-nav{left:0;top:0;width:626px;height:24px;background:rgba(30,4,8,.6)}
.p-nav a{position:absolute;top:7px;color:#fff;font-size:6.5px;text-decoration:none}
.p-nav .sep{position:absolute;top:3px;width:1px;height:18px;background:rgba(255,255,255,.18)}
.p-logo{left:278px;top:0;width:112px;height:54px}
.p-logo span{position:absolute;left:0;top:22px;width:112px;text-align:center;font-family:"Philosopher",serif;font-size:10px;color:#fff}
.p-hours{left:488px;top:59px;font-family:"Lora",serif;font-style:italic;font-size:6px;color:var(--gold)}
.p-title{left:53px;top:76px;font-family:"Roboto",sans-serif;font-weight:700;font-size:22px;line-height:24px;color:#fff;letter-spacing:.3px}
.p-copy{left:56px;top:150px;width:196px;font-size:6px;line-height:12.1px;color:var(--text-light)}
.p-btn{left:56px;top:260px;width:44px;height:12px;font-size:6.5px;line-height:12px;padding-left:4px}
.p-res-link{left:408px;top:268px;font-family:"Lora",serif;font-style:italic;font-size:6.5px;color:var(--gold)}

.p-res{left:0;top:288px;width:626px;height:262px;
  background:linear-gradient(90deg,#efe6da 0%,#f3ece2 60%,#e9dccb 93%,#7a1420 93%,#5a0b13 100%)}
.p-res h2{position:absolute;left:53px;top:26px;font-family:"Josefin Sans",sans-serif;font-weight:300;font-size:19px;line-height:20px;color:var(--red-text)}
.p-res .txt{position:absolute;left:54px;top:75px;width:190px;font-size:5.8px;line-height:12px;color:var(--grey-text)}
.p-res .txt p{margin-bottom:12px}
.form{left:358px;top:12px;width:197px;height:226px;background:#2c0a08;border-radius:2px}
.form h3{height:20px;background:var(--red);color:#fff;font-size:8.5px;font-weight:600;line-height:20px;padding-left:8px;border-radius:2px 2px 0 0}
.form label{position:absolute;font-family:"Philosopher",serif;font-variant:small-caps;font-size:6.5px;line-height:7px;color:#f0e3c8}
.form .field{position:absolute;width:86px;height:11px;background:var(--olive);border:1px solid #b19a26}
.form .area{position:absolute;left:8px;top:148px;width:181px;height:41px;background:var(--olive);border:1px solid #b19a26}
.form .submit{position:absolute;left:38px;top:195px;width:118px;height:26px;background:var(--red);border:2px solid #e0796f;color:#fff;font-size:11px;line-height:22px;padding-left:30px}
.form .submit svg{position:absolute;left:5px;top:3px}
.form-tip{left:455px;top:238px}

.p-test{left:0;top:550px;width:626px;height:331px;
  background:radial-gradient(ellipse at 50% 40%,#4a2614 0%,#2a1208 55%,#140804 100%)}
.p-test h2{position:absolute;left:0;top:20px;width:626px;text-align:center;font-family:"Josefin Sans",sans-serif;font-weight:600;font-size:19px;color:var(--gold)}
.p-test .sub{position:absolute;left:0;top:46px;width:626px;text-align:center;font-family:"Open Sans",sans-serif;font-style:italic;font-weight:600;font-size:8.5px;color:#fff}
.rank-bar{left:55px;top:74px;width:501px;height:16px;background:var(--gold);font-size:6px;line-height:16px;color:#3a2a14;padding:0 5px}
.rank-bar .dot{display:inline-block;width:7px;height:7px;border-radius:50%;background:#3a2a14;vertical-align:-1px;margin:0 2px 0 6px}
.rank-bar .brand{font-weight:600}
.rank-bar .right{position:absolute;right:6px;top:0}
.card{position:absolute;top:109px;width:92px;height:173px;background:#eee9e3}
.card .head{height:69px;background:var(--gold)}
.card.alt .head{background:var(--red)}
.card .avatar{position:absolute;left:24px;top:6px;width:46px;height:46px;border-radius:50%;border:2px solid #fff;background:radial-gradient(circle at 50% 40%,#c9a48a,#6d4a3a)}
.card .name{position:absolute;top:56px;width:92px;text-align:center;font-style:italic;font-size:6px;color:#3a1a10}
.card .ttl{position:absolute;top:76px;width:92px;text-align:center;font-family:"Philosopher",serif;font-variant:small-caps;font-size:6px;color:var(--red-text)}
.card .q{position:absolute;left:4px;top:86px;font-family:"Lora",serif;font-size:11px;color:#555}
.card .body{position:absolute;left:12px;top:90px;width:76px;font-size:5px;line-height:10.4px;color:#444}
.card .date{position:absolute;right:3px;bottom:3px;font-size:3.8px;color:#666}
.test-btn{left:286px;top:366px;width:44px;height:13px;font-size:6.5px;line-height:13px;padding-left:4px;clip-path:none}

.p-mission{left:0;top:881px;width:348px;height:229px;background:var(--gold)}
.p-mission .photo{position:absolute;left:0;top:0;width:130px;height:229px;background:linear-gradient(180deg,#d9be78,#c7a25f 40%,#3b3f55 75%,#b98e4a)}
.p-mission h2{position:absolute;left:132px;top:21px;font-family:"Josefin Sans",sans-serif;font-weight:700;font-size:20px;color:var(--red-text)}
.p-mission .txt{position:absolute;left:134px;top:56px;width:182px;font-size:5.7px;line-height:13px;color:#4a3a20}
.p-mission .txt p{margin-bottom:13px}

.p-contact{left:348px;top:881px;width:138px;height:229px;background:#3a2418}
.p-contact h2{position:absolute;left:8px;top:17px;font-family:"Josefin Sans",sans-serif;font-weight:700;font-size:18px;color:#fff}
.p-contact .info{position:absolute;left:0;top:49px;width:138px;height:180px;background:var(--blue)}
.p-contact .info p{position:absolute;font-size:5.8px;color:#fff}
.feed{left:9px;top:95px;width:120px;height:123px;background:#8c8c88;padding:5px}
.feed-inner{width:110px;height:113px;background:#fff}
.feed-cover{position:absolute;left:8px;top:9px;width:96px;height:46px;background:linear-gradient(135deg,#a3202c,#3a060c)}
.feed-name{position:absolute;left:31px;top:11px;font-size:6px;font-weight:600;color:#fff}
.feed-count{position:absolute;left:31px;top:19px;font-size:4.3px;color:#fff}
.feed-like{position:absolute;left:12px;top:44px;width:44px;height:8px;background:#eee;font-size:4px;line-height:8px;padding-left:2px;color:#333}
.feed-txt{position:absolute;left:12px;top:63px;width:90px;font-size:4.3px;line-height:6px;color:#333}
.feed-faces{position:absolute;left:12px;top:78px;width:70px;height:11px;background:linear-gradient(90deg,#c9a48a,#6d4a3a,#c9a48a,#6d4a3a)}

.p-map{left:486px;top:881px;width:140px;height:229px;background:linear-gradient(135deg,#eceae4,#e2ddd3)}

.p-foot{left:0;top:1110px;width:626px;height:21px;background:#0e0706}
.p-foot .copy{position:absolute;left:55px;top:7px;font-size:4.5px;color:#5a4a3a}
.p-foot .follow{position:absolute;left:356px;top:5px;font-size:7.5px;color:#fff}
.p-foot .soc{position:absolute;top:4px;width:12px;height:12px;border-radius:50%;border:1px solid #fff}
</style>
</head>
<body>

<!-- Large hero -->
<section class="abs hero">
  <div class="abs hero-photo" role="img" aria-label="Dim red dining room with a woman in a red hat and a man in a suit beneath fringed lamps"></div>
  <div class="abs hero-base"></div>
  <nav class="abs hero-nav sc">
    <a style="left:146px">Home</a><span class="sep" style="left:207px"></span>
    <a style="left:238px">About Us</a><span class="sep" style="left:318px"></span>
    <a style="left:350px">Menu</a>
    <svg class="abs" style="left:404px;top:22px" width="8" height="6" viewBox="0 0 8 6"><path d="M1 1l3 3 3-3" stroke="#fff" stroke-width="1.3" fill="none"/></svg>
    <span class="sep" style="left:423px"></span>
    <a style="left:454px;color:var(--gold)">Buy Wine</a>
    <a style="left:728px">Reservations</a><span class="sep" style="left:835px"></span>
    <a style="left:867px">Testimonials</a><span class="sep" style="left:965px"></span>
    <a style="left:995px">Contact</a>
  </nav>
  <div class="abs hero-logo">
    <svg width="176" height="66" viewBox="0 0 176 66"><polygon points="52,0 124,0 176,66 0,66" fill="#e6cc86"/></svg>
    <span>Vellora</span>
  </div>
  <div class="abs hero-hours">Open daily from 5 to 12 am</div>
  <h1 class="abs hero-title">Vellora Bistro<br>italian restaurant<br>in Cabo San Lucas</h1>
  <p class="abs hero-copy">Vellora Bistro Located in the heart of downtown, across from Plaza Marisol, just two short blocks up from Harborview Resort and the Cabo marina is Vellora Bistro, a place with great original Southern Italian and Mediterranean cuisine and a European touch. Sure to enjoy your classic favorites or satisfy even the most distinctive pallet We offer, a variety of homemade , fresh cooked dishes .</p>
  <div class="abs hero-btn btn-gold sc">Read More</div>
</section>

<!-- One-page site -->
<main class="abs page">

  <section class="abs p-hero">
    <div class="abs p-hero-photo" role="img" aria-label="Couple at a small table in a red-lit dining room"></div>
    <nav class="abs p-nav sc">
      <a style="left:76px">Home</a><span class="sep" style="left:122px"></span>
      <a style="left:124px">About Us</a><span class="sep" style="left:180px"></span>
      <a style="left:183px">Menu</a><span class="sep" style="left:213px"></span>
      <a style="left:231px">Buy Wine &amp; Gift</a>
      <a style="left:380px">Reservations</a><span class="sep" style="left:441px"></span>
      <a style="left:452px">Testimonials</a><span class="sep" style="left:503px"></span>
      <a style="left:519px">Contact</a>
    </nav>
    <div class="abs p-logo">
      <svg width="112" height="54" viewBox="0 0 112 54"><path d="M20 0H92L112 48Q112 54 106 54H6Q0 54 0 48Z" fill="#c9a55a"/></svg>
      <span>Vellora</span>
    </div>
    <div class="abs p-hours">Open daily from 5 to 12 am</div>
    <h2 class="abs p-title">Vellora Bistro<br>italian restaurant<br>in Cabo San Lucas</h2>
    <p class="abs p-copy">Vellora Bistro Located in the heart of downtown, across from Plaza Marisol, just two short blocks up from Harborview Resort and the Cabo marina is Vellora Bistro, a place with great original Southern Italian and Mediterranean cuisine and a European touch. Sure to enjoy your classic favorites or satisfy even the most distinctive pallet We offer, a variety of homemade , fresh cooked dishes .</p>
    <div class="abs p-btn btn-gold sc">Read More</div>
    <svg class="abs" style="left:393px;top:259px" width="14" height="18" viewBox="0 0 14 18"><path d="M12 2Q3 2 4 12M1 9l3 5 4-4" stroke="var(--gold)" stroke-width="1.5" fill="none"/></svg>
    <div class="abs p-res-link">Reservations for Vellora bistro Cabo San Lucas</div>
  </section>

  <section class="abs p-res">
    <h2>Reservations for<br>Vellora bistro Cabo San Lucas</h2>
    <div class="txt">
      <p>Reservations for Vellora bistro Cabo San Lucas open 7 days. For reservations less than 48 hours in advance, please call us at our local Mexico number: 624 555 0142.</p>
      <p>To make a reservation more than 48 hours in advance, please complete the following form. All official reservations will receive a 10-digit confirmation code. We have a 15 minute tolerance for all reservations.</p>
      <p>Thank you. We look forward to seeing you soon.</p>
    </div>
    <form class="abs form">
      <h3>RESERVATIONS</h3>
      <label style="left:8px;top:27px">Name:</label><span class="field" style="left:8px;top:36px"></span>
      <label style="left:103px;top:27px">Email:</label><span class="field" style="left:103px;top:36px"></span>
      <label style="left:8px;top:55px">Phone Number (Optional):</label><span class="field" style="left:8px;top:64px"></span>
      <label style="left:103px;top:55px">Date:</label><span class="field" style="left:103px;top:64px"></span>
      <label style="left:8px;top:83px">Time:</label><span class="field" style="left:8px;top:92px"></span>
      <label style="left:103px;top:83px">Hotel Name:</label><span class="field" style="left:103px;top:92px"></span>
      <label style="left:8px;top:111px">Room Number:</label><span class="field" style="left:8px;top:120px"></span>
      <label style="left:103px;top:111px">Guest Email:</label><span class="field" style="left:103px;top:120px"></span>
      <label style="left:8px;top:139px">Comments (Optional):</label><span class="area"></span>
      <div class="submit">
        <svg width="18" height="16" viewBox="0 0 18 16"><path d="M2 8h9M8 4l4 4-4 4M14 3v10" stroke="#fff" stroke-width="1.6" fill="none"/></svg>
        Let’s Register
      </div>
    </form>
    <svg class="abs form-tip" width="22" height="12" viewBox="0 0 22 12"><polygon points="0,0 22,0 11,12" fill="#2c0a08"/></svg>
  </section>

  <section class="abs p-test" role="region" aria-label="Guest reviews">
    <div class="abs" role="img" aria-label="Blurred wine bottles in a cellar" style="left:0;top:0;width:626px;height:331px"></div>
    <h2>What’s Our Client’s Say</h2>
    <p class="sub">Don’t just take it from us, let our cutomers do the talking!</p>
    <div class="abs rank-bar sc">Most Recent Traveler Reviews<span class="dot"></span><span class="brand">Wandermeter</span><span class="right">Wandermeter Ranking: #9 of 574 places to eat in Cabo San Lucas</span></div>

    <article class="card" style="left:60px"><div class="head"></div><div class="avatar" role="img" aria-label="Reviewer portrait"></div><div class="name">Tomas</div><div class="ttl">Delicious Italian!</div><div class="q">“</div><p class="body">We went to Vellora Bistro the third night of our stay. The entire staff was very attentive, the food was amazing and we will definitely be back.</p><div class="date">05/31/2017 04:27:10 pm</div></article>
    <article class="card alt" style="left:160px"><div class="head"></div><div class="avatar" role="img" aria-label="Reviewer portrait"></div><div class="name">Lena R</div><div class="ttl">Best Italian in Cabo”</div><div class="q">“</div><p class="body">My wife and two daughters (21 &amp; 18) had a fanstastic dinner here. The service was top notch and the pastas were fresh ! The elder waiter made...More</p><div class="date">05/31/2017 04:27:10 pm</div></article>
    <article class="card" style="left:260px"><div class="head"></div><div class="avatar" role="img" aria-label="Reviewer portrait"></div><div class="name">Marco J</div><div class="ttl">A Surprising Find</div><div class="q">“</div><p class="body">I have extensive experience working within fine dining italian cuisine establishments and this place holds up even to the places I’ve traveled in Italy.</p><div class="date">05/31/2017 04:27:10 pm</div></article>
    <article class="card alt" style="left:360px"><div class="head"></div><div class="avatar" role="img" aria-label="Reviewer portrait"></div><div class="name">Ines C.</div><div class="ttl">Outstanding, Incredible</div><div class="q">“</div><p class="body">love this place the service is great the food is great. had a wonderful time. Thanks, chef Dario for a wonderful dinner.</p><div class="date">05/31/2017 04:27:10 pm</div></article>
    <article class="card" style="left:460px"><div class="head"></div><div class="avatar" role="img" aria-label="Reviewer portrait"></div><div class="name">Clara V</div><div class="ttl">Wonderful Dinner</div><div class="q">“</div><p class="body">Best italian ever!! - this is A Grade. Don’t be fooled by the facade, enjoy an undiscovered gem of Cabo only 2 blocks back from the Main Street.</p><div class="date">05/31/2017 04:27:10 pm</div></article>

    <div class="abs test-btn btn-gold sc">Read More</div>
  </section>

  <section class="abs p-mission">
    <div class="photo" role="img" aria-label="Smiling man in a sweater pointing toward the text"></div>
    <h2>Our mission is simple</h2>
    <div class="txt">
      <p>To gather those who have impacted our lives and supported us in this wonderful town, bring them high quality food and wines, while simultaneously offering affordable prices to locals and visitors.</p>
      <p>We invite you to come and enjoy a glass of wine and to delight in our exquisite range of unique menu options. Created by hands with years of experience in traditional Mediterranean cuisine, our refreshing, family-style salads and tapas, Italian antipastos, fresh seafood dishes, and baked lasagna will transport your senses.</p>
      <p>It will undoubtedly be an unforgettable experience for your pallet!!</p>
    </div>
  </section>

  <section class="abs p-contact">
    <h2>Contact US!</h2>
    <div class="info">
      <p style="left:8px;top:7px">Address:&nbsp; Calle Olivo 12, Centro</p>
      <p style="left:38px;top:20px">Cabo San Lucas, Mexico</p>
      <p style="left:8px;top:33px">Tel:</p>
      <p style="left:38px;top:33px">555 0142</p>
      <svg class="abs" style="left:110px;top:2px" width="20" height="20" viewBox="0 0 20 20"><circle cx="10" cy="10" r="9" fill="#fff"/><path d="M10 4a4 4 0 0 1 4 4c0 3-4 7-4 7s-4-4-4-7a4 4 0 0 1 4-4z" fill="#d64a3a"/></svg>
    </div>
    <div class="abs feed">
      <div class="feed-inner">
        <div class="feed-cover" role="img" aria-label="Restaurant page cover image"></div>
        <div class="feed-name">Vellora Bistro</div>
        <div class="feed-count">3,469 likes</div>
        <div class="feed-like">Like this page</div>
        <p class="feed-txt">Be the first of your friends to like this on Chatterbay.</p>
        <div class="feed-faces" role="img" aria-label="Small follower portraits"></div>
      </div>
    </div>
  </section>

  <div class="abs p-map" role="img" aria-label="Street map of downtown Cabo San Lucas with the restaurant pinned"></div>

  <footer class="abs p-foot">
    <span class="copy">Copyright © 2017 vellorabistro. All Rights Reserved</span>
    <span class="follow">Follow Us:</span>
    <span class="soc" style="left:400px"></span>
    <span class="soc" style="left:417px"></span>
    <span class="soc" style="left:434px"></span>
    <span class="soc" style="left:451px"></span>
    <span class="soc" style="left:468px"></span>
  </footer>
</main>

</body>
</html>
```